Bref créative
quenzol stationary design
Stationary design
Modern
Ling Paoshen
Manager
52/3F Tanshu Road, Taipei,Taiwan
ling@quenzol.com
quenzol.com
I will like to have 12 sheeps jumping around and the design can derive from my logo. We can have characters such as 1: happy / laughing, 2: surprissed, 3: angry, 5: mysterious, 6: hurry and impatient, 7: affraid / chicken-hearted; cowardly, 8: Strong and muscular,
9: brave. Personalities that are fun .
Jumping sheeps

```html
<!DOCTYPE html>
<html lang="en">
<head>
<meta charset="utf-8">
<title>quenzol business cards</title>
<link href="https://fonts.googleapis.com/css2?family=Nunito:wght@400;600;800&display=swap" rel="stylesheet">
<style>
  :root {
    --backdrop: #7a4a24;
    --card: #ffffff;
    --navy: #1f2a6c;
    --navy-light: #3b4a9c;
    --ink: #2a2a2a;
    --muted: #6b6b6b;
    --rule: #c9c9c9;
  }
  * { margin: 0; padding: 0; box-sizing: border-box; }
  html, body { width: 1200px; height: 403px; overflow: hidden; }
  body {
    background: var(--backdrop);
    font-family: "Nunito", sans-serif;
    position: relative;
  }
  .card {
    position: absolute;
    top: 29px;
    width: 528px;
    height: 345px;
    background: var(--card);
    border-radius: 18px;
    overflow: hidden;
  }
  .card--front { left: 48px; }
  .card--back { left: 643px; }

  .brand {
    position: absolute;
    color: var(--navy);
    font-weight: 800;
    letter-spacing: -1px;
    display: flex;
    align-items: center;
  }
  .brand__dot {
    display: inline-block;
    border-radius: 50%;
    background: var(--navy);
  }
  .card--front .brand { left: 34px; top: 180px; font-size: 50px; gap: 10px; }
  .card--front .brand__dot { width: 18px; height: 18px; }
  .card--back .brand { left: 0; right: 0; justify-content: center; top: 196px; font-size: 64px; gap: 12px; }
  .card--back .brand__dot { width: 22px; height: 22px; }

  .divider {
    position: absolute;
    left: 317px;
    top: 67px;
    width: 1px;
    height: 228px;
    background: var(--rule);
  }
  .contact {
    position: absolute;
    left: 336px;
    top: 60px;
    color: var(--ink);
    font-size: 13px;
    line-height: 1.5;
  }
  .contact__name { font-size: 17px; font-weight: 600; line-height: 1.2; }
  .contact__role { font-size: 12px; color: var(--muted); margin-bottom: 40px; }
  .contact__address { margin-bottom: 42px; }
  .contact__lines { list-style: none; font-size: 12.5px; line-height: 1.55; }

  .band {
    position: absolute;
    left: 0; right: 0; bottom: 0;
    height: 38px;
    background: linear-gradient(180deg, var(--navy-light), var(--navy));
    color: #fff;
    font-size: 12px;
    display: flex;
    align-items: center;
    justify-content: center;
  }
  .web {
    position: absolute;
    left: 0; right: 0; bottom: 18px;
    text-align: center;
    color: var(--muted);
    font-size: 12px;
  }
</style>
</head>
<body>
  <section class="card card--front">
    <div class="brand"><span class="brand__dot"></span>quenzol</div>
    <div class="divider"></div>
    <div class="contact">
      <p class="contact__name">Ling Paoshen</p>
      <p class="contact__role">Manager</p>
      <p class="contact__address">52/3F Tanshu Road,<br>Taipei, Taiwan</p>
      <ul class="contact__lines">
        <li>F : 886-24417305</li>
        <li>C : 886-913560248</li>
        <li>F : 886-24417306</li>
        <li>E : ling@quenzol.com</li>
      </ul>
    </div>
    <div class="band">www.quenzol.com</div>
  </section>

  <section class="card card--back">
    <div class="brand"><span class="brand__dot"></span>quenzol</div>
    <p class="web">www.quenzol.com</p>
  </section>
</body>
</html>
```